We are opening a new restaurant concept called Lanternleaf - Fresh Asian Cuisine. Will be a trendy, casual dining restaurant (somewhat similar to a QR Morvins).
I have included pics of our logo in different formats and a picture of our front menu cover and inside menu as well as our actual menu in draft format. Need 6 individual pages total and letter size. Inside cover would be a "about us" type page that describes who we are and mission statement of restaurant (script unwritten at this time), Next page would be appetizers, inside page would have entrees on left and right side of book, then noodles/rice, vegetarian, kids and dessert section, last page would be drink/cocktail menu (still in progress).

```html
<!DOCTYPE html>
<html lang="en">
<head>
<meta charset="utf-8">
<title>Lanternleaf – Appetizers Menu</title>
<link href="https://fonts.googleapis.com/css2?family=Inconsolata:wght@400;700&family=Montserrat:wght@800&display=swap" rel="stylesheet">
<style>
  :root {
    --backdrop: #ebe8e3;
    --paper: #ffffff;
    --panel: #fdf3f2;
    --panel-border: #e8b9b6;
    --red: #e41e26;
    --ink: #1d1d1d;
    --ink-soft: #333333;
    --photo-rolls: linear-gradient(135deg, #f4c27a 0%, #e9a24a 40%, #9fbf6a 75%, #f1e1c4 100%);
    --photo-chicken: linear-gradient(160deg, #b4532a 0%, #d98a4a 50%, #f2ece4 100%);
    --photo-stirfry: linear-gradient(160deg, #8a5a3a 0%, #6f9a4a 45%, #d8c7a8 100%);
    --photo-orange: linear-gradient(150deg, #e9dccb 0%, #e07a22 35%, #c24d12 70%, #8a3a12 100%);
  }
  html, body {
    margin: 0;
    width: 1200px;
    height: 900px;
    overflow: hidden;
    background: var(--backdrop);
  }
  .stage {
    position: relative;
    width: 1200px;
    height: 900px;
  }
  .menu-page {
    position: absolute;
    left: 297px;
    top: 23px;
    width: 496px;
    height: 700px;
    background: var(--paper);
    transform: scale(1.22);
    transform-origin: 0 0;
    box-shadow: 0 2px 6px rgba(0,0,0,0.15);
    font-family: "Inconsolata", monospace;
    color: var(--ink);
    overflow: hidden;
  }
  .page-title {
    position: absolute;
    left: 30px;
    top: 26px;
    margin: 0;
    font-family: "Montserrat", sans-serif;
    font-weight: 800;
    font-size: 29px;
    letter-spacing: -0.5px;
    text-decoration: underline;
    text-decoration-thickness: 2px;
    text-underline-offset: 3px;
  }
  .menu-panel {
    position: absolute;
    background: var(--panel);
    border: 1px solid var(--panel-border);
    display: flex;
    flex-direction: column;
    justify-content: space-between;
    box-sizing: border-box;
  }
  .panel-left {
    left: 28px;
    top: 75px;
    width: 170px;
    height: 437px;
    padding: 10px 6px 10px 8px;
  }
  .panel-right {
    left: 300px;
    top: 205px;
    width: 168px;
    height: 413px;
    padding: 10px 6px 14px 6px;
  }
  .dish-name {
    display: flex;
    justify-content: space-between;
    font-size: 11px;
    line-height: 1.1;
    margin: 0 0 3px;
  }
  .dish-desc {
    font-size: 5.6px;
    line-height: 1.3;
    color: var(--ink-soft);
    margin: 0;
    max-width: 150px;
  }
  .photo {
    position: absolute;
    box-sizing: border-box;
  }
  .photo-spring-rolls {
    left: 196px; top: 0; width: 300px; height: 203px;
    background: var(--photo-rolls);
    border-left: 7px solid var(--red);
    border-bottom: 8px solid var(--red);
  }
  .photo-sesame-chicken {
    left: 196px; top: 212px; width: 104px; height: 136px;
    background: var(--photo-chicken);
    border: 2px solid var(--red);
  }
  .photo-stir-fry {
    left: 196px; top: 358px; width: 104px; height: 144px;
    background: var(--photo-stirfry);
    border: 2px solid var(--red);
  }
  .photo-orange-chicken {
    left: 0; top: 512px; width: 300px; height: 188px;
    background: var(--photo-orange);
    border-top: 8px solid var(--red);
    border-right: 4px solid var(--red);
  }
  .brand {
    position: absolute;
    left: 334px;
    top: 636px;
    width: 134px;
    text-align: right;
    color: var(--ink);
  }
  .brand-name {
    display: flex;
    align-items: center;
    justify-content: flex-end;
    gap: 5px;
    font-weight: 700;
    font-size: 19px;
    letter-spacing: -0.3px;
    line-height: 1;
  }
  .brand-dot {
    width: 10px; height: 10px;
    border-radius: 50%;
    background: var(--red);
  }
  .brand-tagline {
    font-size: 6px;
    font-weight: 700;
    letter-spacing: 1px;
    margin-top: 2px;
  }
</style>
</head>
<body>
<div class="stage">
  <article class="menu-page">
    <h1 class="page-title">Appetizers</h1>

    <div class="photo photo-spring-rolls" role="img" aria-label="Platter of spring rolls, wontons and fresh salad with dipping sauce"></div>

    <section class="menu-panel panel-left">
      <div class="dish"><p class="dish-name"><span>Edamame</span><span>$4</span></p><p class="dish-desc">Seasoned &amp; boiled soy bean</p></div>
      <div class="dish"><p class="dish-name"><span>Scallion Pancakes</span><span>$6</span></p><p class="dish-desc">Traditional Chinese flatbread folded with oil and minced scallions and pan fried</p></div>
      <div class="dish"><p class="dish-name"><span>Lanternleaf Lettuce Wraps</span><span>$8</span></p><p class="dish-desc">Seasoned ground chicken wrapped in lettuce and drizzled with our secret sauce</p></div>
      <div class="dish"><p class="dish-name"><span>Salt &amp; Pepper Calamari</span><span>$9</span></p><p class="dish-desc">Crispy Calamari with Green &amp; red peppers and onions</p></div>
      <div class="dish"><p class="dish-name"><span>Singapore Ribs</span><span>$9</span></p><p class="dish-desc">Tender baby back ribs in a sweet homemade glaze</p></div>
      <div class="dish"><p class="dish-name"><span>Spicy Bang Bang Shrimp</span><span>$9</span></p><p class="dish-desc">Crispy fried shrimp tossed in our creamy spicy sauce</p></div>
      <div class="dish"><p class="dish-name"><span>Drunken Chicken</span><span>$8</span></p><p class="dish-desc">Chicken, Thai chili and a house made spicy sauce</p></div>
      <div class="dish"><p class="dish-name"><span>Sichuan Spiced Beef</span><span>$9</span></p><p class="dish-desc">Beef Shank, beef tripe, cilantro, peanuts and celery</p></div>
      <div class="dish"><p class="dish-name"><span>Beef Crispy Bottom Bow</span><span>$10</span></p><p class="dish-desc">Pan fried crispy bottom Bao, stuffed with beef, drizzled with scallion and sesame</p></div>
    </section>

    <div class="photo photo-sesame-chicken" role="img" aria-label="Plate of glazed chicken with red chilies"></div>
    <div class="photo photo-stir-fry" role="img" aria-label="Vegetable and meat stir-fry with snow peas and baby corn"></div>

    <section class="menu-panel panel-right">
      <div class="dish"><p class="dish-name"><span>Crispy Mala Beef Jerky</span><span>$9</span></p><p class="dish-desc">Dry fried shredded beef with fresh celery, Serrano peppers, garlic, green onion in soy sauce and peppercorn oil</p></div>
      <div class="dish"><p class="dish-name"><span>Steamed Chicken Dumplings (6)</span><span>$6</span></p><p class="dish-desc">Chinese dumpling stuffed with Chicken, Shiitake mushrooms and bamboo shoots</p></div>
      <div class="dish"><p class="dish-name"><span>Red Oil Dumplings (6)</span><span>$7</span></p><p class="dish-desc">Pork filled dumplings in Sichuan red oil sauce drizzled with sesame</p></div>
      <div class="dish"><p class="dish-name"><span>Pork Egg Rolls (2)</span><span>$4</span></p><p class="dish-desc">Hand rolled with julienned veggies with our sweet n' sour mustard sauce</p></div>
      <div class="dish"><p class="dish-name"><span>Vegetarian Spring Rolls (3)</span><span>$4</span></p><p class="dish-desc">Fresh rice paper roll filled with vermicelli, bean sprouts and lettuce. Served with peanut sauce</p></div>
      <div class="dish"><p class="dish-name"><span>Garlic Cucumber Salad</span><span>$7</span></p><p class="dish-desc">Sliced cucumber with a garlic vinaigrette</p></div>
      <div class="dish"><p class="dish-name"><span>Lanternleaf Hot n' Sour Soup</span><span>$4</span></p><p class="dish-desc">Tangy broth with Bamboo shoot, wood ear fungus, tofu, egg and carrots</p></div>
      <div class="dish"><p class="dish-name"><span>West Lake Soup</span><span>$4</span></p><p class="dish-desc">Light creamy soup with ground beef, diced Shiitake mushroom, tofu, bamboo shoots, egg white and cilantro</p></div>
    </section>

    <div class="photo photo-orange-chicken" role="img" aria-label="Plate of orange chicken garnished with scallions"></div>

    <div class="brand">
      <div class="brand-name"><span class="brand-dot"></span><span>Lanternleaf</span></div>
      <div class="brand-tagline">FRESH ASIAN CUISINE</div>
    </div>
  </article>
</div>
</body>
</html>
```